Natural Organic Cosmetics needs a packaging design

I need package design designs for an organic, natural, unrefined shea butter packaged in a pouch like the example below. The package design should express pure, organic, freshness, moisturizing and healthy. The package design should also reflect the benefits of the product listed below. The product will be called “ORGANIC SHEA BUTTER”
MEANING OF NAME: ZENO AFRICA" meaning to Come to Africa for your natural cosmetics
Logo Text/Brand Name:
“TEVO”
Logo Styles of Interest:
Elegance
Natural
Organic
Freshness
Unrefined
From a tree nut
Target Market:
General public
Must have:
KISS : Keep it simple stupid
Note: I have a shea nuts stock photo i can provide.
Dimension:W = 7.48 InchesH = 10.43 inches Added Thursday, January 14, 2016
Industry/Entity Type
Cosmetics

```html
<!DOCTYPE html>
<html lang="en">
<head>
<meta charset="utf-8">
<title>TEVO Shea Butter Pouch</title>
<link href="https://fonts.googleapis.com/css2?family=Montserrat:wght@400;500;600;900&display=swap" rel="stylesheet">
<style>
  :root {
    --stage-top: #c4c4c4;
    --stage-bottom: #e8e8e8;
    --mint: #8fcfb6;
    --mint-deep: #76b9a1;
    --pill: #8fd0b4;
    --seal: #0f3d44;
    --seal-inner: #8fcfb6;
    --kraft: #e09a62;
    --kraft-edge: #c9824c;
    --ink: #161616;
    --white: #ffffff;
    --twine: #8a5a38;
    --nut-light: #d8bc92;
    --nut-mid: #a9794a;
  }
  html, body {
    margin: 0;
    padding: 0;
    width: 1200px;
    height: 1200px;
    overflow: hidden;
  }
  .canvas {
    position: relative;
    width: 1200px;
    height: 1200px;
    background: linear-gradient(var(--stage-top), var(--stage-bottom));
    font-family: "Montserrat", sans-serif;
  }
  .pouch {
    position: absolute;
    left: 275px;
    top: 62px;
    width: 645px;
    height: 1088px;
    background: var(--mint);
    overflow: hidden;
  }
  .seal-band {
    position: absolute;
    left: 0; top: 0;
    width: 100%;
    height: 70px;
    background: var(--mint-deep);
  }
  .product-photo {
    position: absolute;
    left: 0;
    top: 700px;
    width: 100%;
    height: 388px;
    background: radial-gradient(ellipse at 45% 55%, var(--nut-mid) 0%, var(--nut-light) 55%, #e7d6b8 100%);
  }
  .brand {
    position: absolute;
    left: 0;
    top: 133px;
    width: 100%;
    margin: 0;
    text-align: center;
    color: var(--white);
    font-weight: 900;
    font-size: 130px;
    line-height: 1;
  }
  .organic-seal {
    position: absolute;
    left: 242px;
    top: 325px;
    width: 170px;
    height: 170px;
    border-radius: 50%;
    background: var(--seal);
    z-index: 3;
  }
  .organic-seal::after {
    content: "";
    position: absolute;
    left: 45px;
    top: 45px;
    width: 80px;
    height: 80px;
    border-radius: 50%;
    background: var(--seal-inner);
  }
  .twine {
    position: absolute;
    left: 0; top: 0;
    z-index: 4;
  }
  .tag {
    position: absolute;
    left: -15px;
    top: 518px;
    width: 700px;
    height: 280px;
    transform: rotate(14deg);
    transform-origin: 50% 50%;
    z-index: 2;
  }
  .tag-shape { position: absolute; left: 0; top: 0; }
  .tag-pill {
    position: absolute;
    left: 180px;
    top: 48px;
    width: 350px;
    height: 76px;
    border-radius: 16px;
    background: var(--pill);
    color: var(--white);
    font-weight: 500;
    font-size: 42px;
    line-height: 76px;
    text-align: center;
    white-space: nowrap;
  }
  .tag-title {
    position: absolute;
    left: 73px;
    top: 150px;
    width: 540px;
    text-align: center;
    color: var(--ink);
    font-weight: 500;
    font-size: 70px;
    line-height: 1;
    white-space: nowrap;
  }
  .tag-origin {
    position: absolute;
    left: 236px;
    top: 240px;
    color: var(--ink);
    font-weight: 600;
    font-size: 19px;
    white-space: nowrap;
  }
  .net-weight {
    position: absolute;
    left: 0;
    top: 895px;
    width: 100%;
    text-align: center;
    color: var(--white);
    font-weight: 600;
    font-size: 22px;
  }
  .divider {
    position: absolute;
    left: 92px;
    top: 958px;
    width: 460px;
    height: 2px;
    background: var(--white);
  }
  .usage-note {
    position: absolute;
    left: 0;
    top: 993px;
    width: 100%;
    text-align: center;
    color: var(--white);
    font-weight: 500;
    font-size: 18px;
  }
</style>
</head>
<body>
<main class="canvas">
  <section class="pouch">
    <div class="seal-band"></div>
    <div class="product-photo" role="img" aria-label="Photo of whole shea nuts and sage leaves in a wooden bowl"></div>

    <h1 class="brand">TEVO</h1>

    <div class="organic-seal"></div>

    <div class="tag">
      <svg class="tag-shape" width="700" height="280" viewBox="0 0 700 280">
        <polygon points="60,0 700,0 700,280 60,280 0,220 0,60" fill="var(--kraft)" stroke="var(--kraft-edge)" stroke-width="2"/>
        <circle cx="38" cy="140" r="10" fill="var(--mint)" stroke="var(--kraft-edge)" stroke-width="2"/>
      </svg>
      <div class="tag-pill">100% NATURAL</div>
      <div class="tag-title">SHEA BUTTER</div>
      <div class="tag-origin">Produced in Ghana</div>
    </div>

    <svg class="twine" width="645" height="700" viewBox="0 0 645 700">
      <path d="M262 13 C 190 170, 90 360, 28 580" fill="none" stroke="var(--twine)" stroke-width="5"/>
      <path d="M276 13 C 210 170, 110 360, 38 580" fill="none" stroke="var(--twine)" stroke-width="4"/>
    </svg>

    <div class="net-weight">16 OZ.</div>
    <div class="divider"></div>
    <div class="usage-note">External Use Only</div>
  </section>
</main>
</body>
</html>
```